An PLX basketball and news website

With the frenzy of basketball activities and huge audience in the Americas and Europe. I am looking for a glossy website which deals on the events and happening of PLX basketball league. The website is to cover news, events, scores and interviews with professional basketballer. The website will also cover other basketball events around the world such as the ORUN world basketball championships. My target audience are Americans. I will prefer bright colors for my website. There will be a category for live basketball matches. Also fans will also be able on comment on the news column under the news iteam.

Industry/Entity Type

Events

```html
<!DOCTYPE html>
<html lang="en">
<head>
<meta charset="utf-8">
<title>Basketball — PLX League News</title>
<link href="https://fonts.googleapis.com/css2?family=Raleway:ital,wght@0,400;0,500;0,600;0,700;1,500&family=Open+Sans:ital,wght@0,400;0,600;1,400&display=swap" rel="stylesheet">
<style>
:root{
  --orange:#e84c33;
  --orange-soft:#f0735c;
  --ink:#1b1b1b;
  --text:#333;
  --muted:#8a8a8a;
  --rule:#d9d9d9;
  --black:#000;
  --footer:#2b2b2b;
  --footer-line:#444;
  --white:#fff;
}
*{box-sizing:border-box;margin:0;padding:0}
html,body{width:1200px;height:2691px;overflow:hidden;background:var(--white)}
body{position:relative;font-family:"Open Sans",Arial,sans-serif;color:var(--text)}
ul{list-style:none}
.abs{position:absolute}
.heading{font-family:"Raleway",Arial,sans-serif;font-weight:500;color:var(--orange)}

/* header */
.site-header{position:absolute;left:0;top:0;width:1200px;height:104px;background:var(--white)}
.brand{position:absolute;left:50px;top:22px;font-family:"Raleway",Arial,sans-serif;font-weight:600;font-size:52px;line-height:60px;color:var(--orange);letter-spacing:-0.5px}
.main-nav{position:absolute;left:506px;top:0;height:104px;display:flex}
.main-nav li{height:104px;display:flex;align-items:center;justify-content:center;font-family:"Open Sans",Arial,sans-serif;font-size:11px;color:#444;text-transform:uppercase;letter-spacing:.3px}
.main-nav li.active{background:var(--orange);color:var(--white)}

/* hero */
.hero{position:absolute;left:0;top:104px;width:1200px;height:632px;background:linear-gradient(170deg,#1c4fa6 0%,#2a6cc6 45%,#7fb0e0 85%,#dce9f5 100%)}
.hero-feed{position:absolute;left:827px;top:66px;width:323px;height:505px;background:rgba(0,0,0,.92)}
.hero-feed .chev{position:absolute;left:148px}
.feed-item{position:absolute;left:13px;width:292px;height:98px;border:1px solid #7a2a1d;display:flex;align-items:center;padding-left:10px}
.feed-thumb{width:103px;height:68px;flex:none;background:linear-gradient(135deg,#2f5fb0,#c98a4b)}
.feed-body{margin-left:12px;font-size:9.5px;line-height:14px;color:var(--white)}
.feed-body .tag,.feed-body .more{color:var(--orange);text-transform:uppercase;font-weight:600}

/* news */
.lead-photo{left:47px;top:782px;width:579px;height:233px;background:linear-gradient(120deg,#b85a2a,#1d2a4a 55%,#c27a3f)}
.lead-title{left:47px;top:1025px;width:585px;font-family:"Raleway",Arial,sans-serif;font-weight:600;font-size:17px;line-height:24px;color:var(--ink)}
.lead-text{left:47px;top:1077px;width:585px;font-size:11px;line-height:20px;color:#666}
.dot-arrow{display:inline-block;width:11px;height:11px;border-radius:50%;background:var(--orange);vertical-align:middle;margin-left:6px;position:relative}
.dot-arrow::after{content:"";position:absolute;left:4px;top:3px;border-left:4px solid #fff;border-top:2.5px solid transparent;border-bottom:2.5px solid transparent}
.breaking-title{left:671px;top:772px;font-size:29px}
.view-all{left:1098px;top:780px;font-size:11px;color:var(--orange)}
.news-row{position:absolute;left:678px;width:470px;height:88px}
.news-row .thumb{position:absolute;left:0;top:0;width:102px;height:82px;background:linear-gradient(140deg,#8a4a2c,#2d3b66)}
.news-row .meta{position:absolute;left:117px;top:-4px;width:353px}
.news-row .date{font-size:10px;color:var(--muted);line-height:16px}
.news-row h3{font-family:"Raleway",Arial,sans-serif;font-weight:700;font-size:16px;line-height:22px;color:var(--ink)}
.news-row p{font-size:10.5px;line-height:16px;color:#666}
.news-row .rule{position:absolute;left:117px;top:88px;width:353px;border-top:2px solid var(--rule)}

/* highlights & video */
.band-orange{left:0;top:1179px;width:890px;height:414px;background:var(--orange)}
.band-black{left:890px;top:1179px;width:310px;height:414px;background:var(--black)}
.band-title{font-family:"Raleway",Arial,sans-serif;font-weight:500;font-size:30px;color:var(--white);line-height:40px}
.title-rule{position:absolute;height:2px;background:rgba(255,255,255,.55)}
.title-ring{position:absolute;width:11px;height:11px;border:2px solid rgba(255,255,255,.75);border-radius:50%}
.clip-card{position:absolute;top:1266px;width:238px;height:264px;background:#f4f4f4;border:3px solid #fbe3dc;box-shadow:0 0 18px rgba(255,255,255,.45)}
.clip-card .still{position:absolute;left:0;top:0;width:100%;height:216px;background:linear-gradient(160deg,#6c2b22,#2c3554 55%,#b23a2c)}
.clip-card .play{position:absolute;left:0;top:216px;width:100%;height:42px;display:flex;align-items:center;justify-content:center;gap:14px;font-family:"Raleway",Arial,sans-serif;font-size:16px;color:var(--orange)}
.pager{left:425px;top:1562px;display:flex;gap:6px;align-items:center}
.pager span{width:9px;height:9px;border-radius:50%;background:var(--white)}
.pager span.on{width:13px;height:13px;background:none;border:2px solid var(--white);position:relative}
.pager span.on::after{content:"";position:absolute;left:2px;top:2px;width:5px;height:5px;border-radius:50%;background:#fff}
.video-menu{left:955px;top:1274px}
.video-menu li{height:57px;display:flex;align-items:center;font-size:13px;color:var(--white);text-transform:uppercase;letter-spacing:.2px}
.video-menu li::before{content:"";border-left:7px solid #fff;border-top:5px solid transparent;border-bottom:5px solid transparent;margin-right:26px}
.video-menu li.current{color:var(--orange)}
.video-menu li.current::before{border-left-color:var(--orange)}

/* reviews & events */
.section-title{font-size:29px}
.grey-rule{position:absolute;height:1px;background:var(--rule)}
.grey-ring{position:absolute;width:11px;height:11px;border:1px solid #aaa;border-radius:50%;background:#fff}
.review{position:absolute;left:47px;width:572px;height:160px}
.review .pic{position:absolute;left:0;top:0;width:244px;height:148px;background:linear-gradient(150deg,#c9c2b4,#3e4a6b 55%,#a34a33)}
.review .copy{position:absolute;left:278px;top:0;width:294px}
.review h4{font-family:"Raleway",Arial,sans-serif;font-style:italic;font-weight:500;font-size:15px;line-height:22px;color:var(--ink)}
.review p{margin-top:8px;font-size:10.5px;line-height:17px;color:#777}
.learn{margin-top:10px;font-size:10.5px;color:#333;display:flex;align-items:center;gap:8px}
.learn.hot{color:var(--orange)}
.learn .tri{border-left:5px solid currentColor;border-top:4px solid transparent;border-bottom:4px solid transparent}
.stars{display:flex;gap:2px;margin-left:8px}
.event{position:absolute;left:709px;width:442px;height:140px}
.event .pic{position:absolute;left:0;top:0;width:134px;height:111px;background:linear-gradient(145deg,#2a3154,#c8c5c0 60%,#8a3a2a)}
.event .copy{position:absolute;left:147px;top:-6px;width:295px}
.event h4{font-family:"Raleway",Arial,sans-serif;font-weight:600;font-size:16px;line-height:24px;color:var(--ink)}
.event p{font-size:10.5px;line-height:21px;color:#777}
.event .posted{font-size:9px;font-style:italic;color:#555;margin-top:4px}
.event .dash{position:absolute;left:0;width:442px;border-top:1px dashed #ccc}

/* footer */
.site-footer{left:0;top:2314px;width:1200px;height:287px;background:var(--footer)}
.foot-col{position:absolute;top:2360px}
.foot-col h5{font-family:"Raleway",Arial,sans-serif;font-weight:600;font-size:15px;color:var(--orange);margin-bottom:12px}
.foot-col li{font-size:10.5px;line-height:28.5px;color:#e6e6e6;padding-left:13px;position:relative}
.foot-col li::before{content:"";position:absolute;left:0;top:13px;width:4px;height:4px;border-radius:50%;background:#ddd}
.foot-divider{position:absolute;top:2350px;width:1px;height:206px;background:var(--footer-line)}
.base-bar{left:0;top:2601px;width:1200px;height:90px;background:var(--orange)}
.copyright{left:0;top:2638px;width:1200px;text-align:center;font-size:10px;color:var(--white)}
.social{position:absolute;top:2632px;width:28px;height:28px;border:1px solid rgba(255,255,255,.85)}
</style>
</head>
<body>

<header class="site-header">
  <div class="brand">Basketball</div>
  <ul class="main-nav">
    <li class="active" style="width:82px">Home</li>
    <li style="width:122px">Abouts Us</li>
    <li style="width:134px">Popular News</li>
    <li style="width:124px">Latest News</li>
    <li style="width:92px">Blogs</li>
    <li style="width:108px">Contact Us</li>
  </ul>
</header>

<section class="hero" role="img" aria-label="Photo of a young player in a blue shirt shooting a ball toward a hoop under a blue sky">
  <aside class="hero-feed">
    <svg class="chev" style="top:12px" width="26" height="14" viewBox="0 0 26 14"><path d="M3 12 L13 3 L23 12" fill="none" stroke="#e84c33" stroke-width="2.5"/></svg>
    <div class="feed-item" style="top:46px"><div class="feed-thumb" role="img" aria-label="Player dunking"></div><div class="feed-body"><div class="tag">Sports</div>Lorem ipsum dolor sit amet,<br>consectetur adipiscing elit<div class="more">Read More</div></div></div>
    <div class="feed-item" style="top:152px"><div class="feed-thumb" role="img" aria-label="Players on court"></div><div class="feed-body"><div class="tag">Sports</div>Lorem ipsum dolor sit amet,<br>consectetur adipiscing elit<div class="more">Read More</div></div></div>
    <div class="feed-item" style="top:259px"><div class="feed-thumb" role="img" aria-label="Game action"></div><div class="feed-body"><div class="tag">Sports</div>Lorem ipsum dolor sit amet,<br>consectetur adipiscing elit<div class="more">Read More</div></div></div>
    <div class="feed-item" style="top:371px"><div class="feed-thumb" role="img" aria-label="Ball dropping through net"></div><div class="feed-body"><div class="tag">Sports</div>Lorem ipsum dolor sit amet,<br>consectetur adipiscing elit<div class="more">Read More</div></div></div>
    <svg class="chev" style="top:478px" width="26" height="14" viewBox="0 0 26 14"><path d="M3 2 L13 11 L23 2" fill="none" stroke="#e84c33" stroke-width="2.5"/></svg>
  </aside>
</section>

<div class="abs lead-photo" role="img" aria-label="Photo of a professional player driving with the ball"></div>
<h2 class="abs lead-title">CPL Indian Pro Basketball League Season 2 Day 7: Rising Delhi and Bengaluru sides</h2>
<p class="abs lead-text">Lorem ipsum dolor sit amet, consectetur adipiscing elit, sed do eiusmod tempor incididunt ut labore et dolore magna aliqua. Ut enim ad minim veniam, quis nostrud exercitation ullamco laboris .<span class="dot-arrow"></span></p>

<h2 class="abs heading breaking-title">Breaking News</h2>
<span class="abs view-all">View All</span>
<article class="news-row" style="top:832px"><div class="thumb" role="img" aria-label="Match photo"></div><div class="meta"><div class="date">12/02/2016</div><h3>Lorem Ipsum Dolor Sit</h3><p>Lorem ipsum dolor sit amet, consectetur adipiscing elit, sed do eiusmod tempor incididunt ut labore</p></div><div class="rule"></div></article>
<article class="news-row" style="top:935px"><div class="thumb" role="img" aria-label="Match photo"></div><div class="meta"><div class="date">24/02/2016</div><h3>Lorem Ipsum Dolor Sit</h3><p>Lorem ipsum dolor sit amet, consectetur adipiscing elit, sed do eiusmod tempor incididunt ut labore</p></div><div class="rule"></div></article>
<article class="news-row" style="top:1037px"><div class="thumb" role="img" aria-label="Match photo"></div><div class="meta"><div class="date">25/02/2016</div><h3>Lorem Ipsum Dolor Sit</h3><p>Lorem ipsum dolor sit amet, consectetur adipiscing elit, sed do eiusmod tempor incididunt ut labore</p></div><div class="rule"></div></article>

<div class="abs band-orange"></div>
<div class="abs band-black"></div>
<h2 class="abs band-title" style="left:57px;top:1196px">Highlights</h2>
<span class="title-ring" style="left:210px;top:1211px"></span>
<span class="title-rule" style="left:222px;top:1216px;width:656px"></span>

<div class="clip-card" style="left:46px"><div class="still" role="img" aria-label="Highlight clip still of players at the rim"></div><div class="play">Play Now <svg width="28" height="20" viewBox="0 0 28 20"><circle cx="14" cy="10" r="9" fill="#e84c33"/><path d="M11 5.5 L18 10 L11 14.5Z" fill="#fff"/></svg></div></div>
<div class="clip-card" style="left:318px"><div class="still" role="img" aria-label="Highlight clip still of a player rising for a dunk"></div><div class="play">Play Now <svg width="28" height="20" viewBox="0 0 28 20"><circle cx="14" cy="10" r="9" fill="#e84c33"/><path d="M11 5.5 L18 10 L11 14.5Z" fill="#fff"/></svg></div></div>
<div class="clip-card" style="left:595px"><div class="still" role="img" aria-label="Highlight clip still of two players in a drive"></div><div class="play">Play Now <svg width="28" height="20" viewBox="0 0 28 20"><circle cx="14" cy="10" r="9" fill="#e84c33"/><path d="M11 5.5 L18 10 L11 14.5Z" fill="#fff"/></svg></div></div>
<div class="abs pager"><span></span><span class="on"></span><span></span></div>

<span class="title-rule" style="left:890px;top:1216px;width:98px"></span>
<span class="title-ring" style="left:986px;top:1211px"></span>
<h2 class="abs band-title" style="left:1005px;top:1196px">Video</h2>
<span class="title-ring" style="left:1090px;top:1211px"></span>
<ul class="abs video-menu">
  <li class="current">Highlights</li>
  <li>Top Plays</li>
  <li>Editor's Picks</li>
  <li>Chennal</li>
  <li>Watch Live</li>
</ul>

<h2 class="abs heading section-title" style="left:54px;top:1639px">Top Reviews</h2>
<span class="grey-ring" style="left:240px;top:1655px"></span>
<span class="grey-rule" style="left:251px;top:1660px;width:368px"></span>

<article class="review" style="top:1713px"><div class="pic" role="img" aria-label="Players contesting a rebound"></div><div class="copy"><h4>Consectetur Adipiscing Aed Eiusmod Tempor edit</h4><p>Lorem ipsum dolor sit amet, consectetur adipiscing elit, sed do eiusmod tempor incididunt ut labore et Ut enim ad minim veniam, sed do eiusmod tempor incididunt ut labore et Ut enim tempor incididunt</p><div class="learn hot">Learn More <span class="tri"></span><span class="stars"><svg width="62" height="11" viewBox="0 0 62 11"><g fill="none" stroke="#e84c33" stroke-width="1"><path d="M5.5 1l1.3 3h3.2l-2.6 2 1 3.2-2.9-1.9-2.9 1.9 1-3.2-2.6-2h3.2z" fill="#e84c33"/><path transform="translate(12 0)" d="M5.5 1l1.3 3h3.2l-2.6 2 1 3.2-2.9-1.9-2.9 1.9 1-3.2-2.6-2h3.2z" fill="#e84c33"/><path transform="translate(24 0)" d="M5.5 1l1.3 3h3.2l-2.6 2 1 3.2-2.9-1.9-2.9 1.9 1-3.2-2.6-2h3.2z"/><path transform="translate(36 0)" d="M5.5 1l1.3 3h3.2l-2.6 2 1 3.2-2.9-1.9-2.9 1.9 1-3.2-2.6-2h3.2z"/><path transform="translate(48 0)" d="M5.5 1l1.3 3h3.2l-2.6 2 1 3.2-2.9-1.9-2.9 1.9 1-3.2-2.6-2h3.2z"/></g></svg></span></div></div></article>
<article class="review" style="top:1886px"><div class="pic" role="img" aria-label="Players in a game under the basket" style="background:linear-gradient(150deg,#e0b25a,#2d3f7a 55%,#c0462f)"></div><div class="copy"><h4>Consectetur Adipiscing Aed Eiusmod Tempor edit</h4><p>Lorem ipsum dolor sit amet, consectetur adipiscing elit, sed do eiusmod tempor incididunt ut labore et Ut enim ad minim veniam, sed do eiusmod tempor incididunt ut labore et Ut enim tempor incididunt</p><div class="learn">Learn More <span class="tri"></span></div></div></article>
<article class="review" style="top:2058px"><div class="pic" role="img" aria-label="Wheelchair basketball game" style="background:linear-gradient(150deg,#1f3f8a,#3b5fb0 50%,#a83a2e)"></div><div class="copy"><h4>Consectetur Adipiscing Aed Eiusmod Tempor edit</h4><p>Lorem ipsum dolor sit amet, consectetur adipiscing elit, sed do eiusmod tempor incididunt ut labore et Ut enim ad minim veniam, sed do eiusmod tempor incididunt ut labore et Ut enim tempor incididunt</p><div class="learn">Learn More <span class="tri"></span></div></div></article>

<h2 class="abs heading section-title" style="left:700px;top:1639px">Upcoming Events</h2>
<span class="grey-ring" style="left:955px;top:1655px"></span>
<span class="grey-rule" style="left:966px;top:1660px;width:185px"></span>

<article class="event" style="top:1708px"><div class="pic" role="img" aria-label="Two players in a close contest"></div><div class="copy"><h4>Lorem ipsum dolor sit amet,</h4><p>Lorem ipsum dolor sit amet, consectetur adipiscing elit, sed do eiusmod tempor incididunt ut labore et dolore magna aliqua.<span class="dot-arrow"></span></p><div class="posted">Posted by 08/02/2016</div></div><div class="dash" style="top:129px"></div></article>
<article class="event" style="top:1855px"><div class="pic" role="img" aria-label="Player dribbling past a defender"></div><div class="copy"><h4>Lorem ipsum dolor sit amet,</h4><p>Lorem ipsum dolor sit amet, consectetur adipiscing elit, sed do eiusmod tempor incididunt ut labore et dolore magna aliqua.<span class="dot-arrow"></span></p><div class="posted">Posted by 08/02/2016</div></div><div class="dash" style="top:139px"></div></article>
<article class="event" style="top:2009px"><div class="pic" role="img" aria-label="Player driving to the basket"></div><div class="copy"><h4>Lorem ipsum dolor sit amet,</h4><p>Lorem ipsum dolor sit amet, consectetur adipiscing elit, sed do eiusmod tempor incididunt ut labore et dolore magna aliqua.<span class="dot-arrow"></span></p><div class="posted">Posted by 08/02/2016</div></div><div class="dash" style="top:134px"></div></article>
<article class="event" style="top:2158px"><div class="pic" role="img" aria-label="Portrait of a professional player" style="background:linear-gradient(145deg,#2c2c3a,#6a4a3e 55%,#1e3c8a)"></div><div class="copy"><h4>Lorem ipsum dolor sit amet,</h4><p>Lorem ipsum dolor sit amet, consectetur adipiscing elit, sed do eiusmod tempor incididunt ut labore et dolore magna aliqua.<span class="dot-arrow"></span></p><div class="posted">Posted by 08/02/2016</div></div></article>

<footer>
  <div class="abs site-footer"></div>
  <span class="foot-divider" style="left:371px"></span>
  <span class="foot-divider" style="left:655px"></span>
  <span class="foot-divider" style="left:936px"></span>
  <div class="foot-col" style="left:118px"><h5>Latest News</h5><ul><li>Breaking News</li><li>Special Video</li><li>Today News</li><li>Contact</li></ul></div>
  <div class="foot-col" style="left:404px"><h5>Important Links</h5><ul><li>Core Team</li><li>Work At Brightcourt</li><li>Privacy Policy</li><li>Terms of Use</li></ul></div>
  <div class="foot-col" style="left:685px"><h5>Categories</h5><ul><li>Webmail Login</li><li>Account Login</li><li>FAQs</li><li>Server References</li></ul></div>
  <div class="foot-col" style="left:969px"><h5>Navigation</h5><ul><li>Home</li><li>About Us</li><li>Tournaments</li><li>Service</li><li>Popular post</li></ul></div>
  <div class="abs base-bar"></div>
  <p class="abs copyright">Copyright 2016 Company Name.&nbsp; All Rights Reserved.</p>
  <span class="social" style="left:1037px"></span>
  <span class="social" style="left:1078px"></span>
  <span class="social" style="left:1120px"></span>
</footer>

</body>
</html>
```